showcase project portfolio

create power point of project portfolio
from word file and website using similar design template

https://www.brelvon.co.uk/

Target Market(s)

corporte

```html
<!DOCTYPE html>
<html lang="en">
<head>
<meta charset="utf-8">
<title>Brelvon Design Solutions – Project Portfolio</title>
<link href="https://fonts.googleapis.com/css2?family=Montserrat:wght@400;500;600;700;800&family=Archivo+Black&display=swap" rel="stylesheet">
<style>
:root{
  --navy:#1f3b53;
  --tan:#cfa98c;
  --tan-light:#d9b595;
  --canvas:#e1e1e1;
  --white:#ffffff;
  --ink:#2a2a2a;
  --muted-blue:#2f6286;
}
*{margin:0;padding:0;box-sizing:border-box}
html,body{width:777px;height:1200px;overflow:hidden}
body{background:var(--canvas);font-family:"Montserrat",sans-serif;color:var(--ink);position:relative}
.top-band{position:absolute;left:0;top:0;width:777px;height:75px;background:var(--tan)}
.slide{position:absolute;width:355px;height:200px;background:var(--white);overflow:hidden}
.col-l{left:27px}.col-r{left:395px}
.r1{top:35px}.r2{top:246px}.r3{top:458px}.r4{top:669px}.r5{top:881px}
.tab{position:absolute;left:0;top:0;height:28px;width:131px;background:var(--navy);
  clip-path:polygon(0 0,100% 0,86% 100%,0 100%);color:var(--tan-light);font-weight:500;
  font-size:11px;letter-spacing:.3px;padding:6px 0 0 15px}
.tab.wide{width:166px}
.footer{position:absolute;left:11px;top:176px;width:334px;height:10px;background:var(--tan);
  display:flex;justify-content:space-between;align-items:center;padding:0 11px;font-size:3.6px;color:var(--ink)}
.photo{position:absolute}
.location{position:absolute;font-weight:800;color:var(--navy);font-size:8px;line-height:1.2;text-transform:uppercase;letter-spacing:.1px}
.proposal{position:absolute;font-size:6.3px;line-height:1.3;color:var(--ink)}
.proposal b{font-weight:700}
.drawing{position:absolute;background:#f1f2f2;border:0.5px solid #d6d8da}
/* cover */
.brand{position:absolute;left:25px;top:30px;display:flex;align-items:center;gap:4px;font-size:6px;font-weight:700;color:var(--navy)}
.brand i{display:block;width:8px;height:8px;background:var(--tan)}
.cover-box{position:absolute;left:23px;top:74px;width:163px;height:102px;background:var(--navy);
  padding:24px 0 0 10px;color:var(--tan-light);font-weight:800;font-size:12px;line-height:15.5px}
.cover-bar{position:absolute;left:23px;top:176px;width:325px;height:10px;background:var(--tan)}
/* tasks */
.tasks{position:absolute;top:35px;list-style:none;width:118px}
.tasks li{display:flex;gap:4px;font-size:5.4px;font-weight:500;line-height:1.2;margin-bottom:5.5px;color:var(--ink)}
.tasks svg{flex:none;width:9px;height:9px}
/* thank you */
.thanks{background:var(--navy)}
.thanks .word{position:absolute;left:156px;color:var(--white);font-family:"Archivo Black",sans-serif;font-size:45px;line-height:1}
.thanks .mark-name{position:absolute;left:11px;top:151px;font-size:7.5px;letter-spacing:1px;color:var(--muted-blue);font-weight:500;text-transform:uppercase}
.fp-title{position:absolute;font-weight:800;color:var(--navy);font-size:8.5px;line-height:1.2}
.elev-label{position:absolute;font-size:3.6px;font-weight:700;color:var(--ink)}
</style>
</head>
<body>
<div class="top-band"></div>

<!-- Cover -->
<section class="slide col-l r1">
  <div class="brand"><i></i>BRELVON</div>
  <div class="photo" role="img" aria-label="Rendered view of a two-storey white house with parked cars" style="left:113px;top:23px;width:234px;height:153px;background:linear-gradient(180deg,#6f9fd6 0%,#a9c6e4 45%,#7e8a7a 70%,#5a5d62 100%)"></div>
  <div class="cover-box">PROJECTS<br>MANAGED BY<br>BRELVON DESIGN<br>SOLUTIONS LTD</div>
  <div class="cover-bar"></div>
</section>

<!-- Project Task -->
<section class="slide col-r r1">
  <div class="photo" role="img" aria-label="Faded green lawn and building backdrop" style="left:268px;top:0;width:87px;height:200px;background:linear-gradient(180deg,#b39e8b 0%,#8a8f7b 40%,#3d6a4c 100%)"></div>
  <div class="tab" style="font-size:15px;padding-top:5px">Project Task</div>
  <ul class="tasks" style="left:15px">
    <li><svg viewBox="0 0 10 10"><circle cx="5" cy="5" r="5" fill="#1f3b53"/><path d="M2.8 5.2l1.5 1.5 3-3.2" stroke="#fff" stroke-width="1.1" fill="none"/></svg>Creating working drawings</li>
    <li><svg viewBox="0 0 10 10"><circle cx="5" cy="5" r="5" fill="#1f3b53"/><path d="M2.8 5.2l1.5 1.5 3-3.2" stroke="#fff" stroke-width="1.1" fill="none"/></svg>Price breakdown of total build costs</li>
    <li><svg viewBox="0 0 10 10"><circle cx="5" cy="5" r="5" fill="#1f3b53"/><path d="M2.8 5.2l1.5 1.5 3-3.2" stroke="#fff" stroke-width="1.1" fill="none"/></svg>Liaising with Vale Waters for water connection, drainage connection</li>
    <li><svg viewBox="0 0 10 10"><circle cx="5" cy="5" r="5" fill="#1f3b53"/><path d="M2.8 5.2l1.5 1.5 3-3.2" stroke="#fff" stroke-width="1.1" fill="none"/></svg>Liaising with Northgas to get gas supply to site</li>
    <li><svg viewBox="0 0 10 10"><circle cx="5" cy="5" r="5" fill="#1f3b53"/><path d="M2.8 5.2l1.5 1.5 3-3.2" stroke="#fff" stroke-width="1.1" fill="none"/></svg>Liaising with GridConnect to get electric supply</li>
    <li><svg viewBox="0 0 10 10"><circle cx="5" cy="5" r="5" fill="#1f3b53"/><path d="M2.8 5.2l1.5 1.5 3-3.2" stroke="#fff" stroke-width="1.1" fill="none"/></svg>Tendering out works to different tradesman</li>
    <li><svg viewBox="0 0 10 10"><circle cx="5" cy="5" r="5" fill="#1f3b53"/><path d="M2.8 5.2l1.5 1.5 3-3.2" stroke="#fff" stroke-width="1.1" fill="none"/></svg>Getting material orders</li>
    <li><svg viewBox="0 0 10 10"><circle cx="5" cy="5" r="5" fill="#1f3b53"/><path d="M2.8 5.2l1.5 1.5 3-3.2" stroke="#fff" stroke-width="1.1" fill="none"/></svg>Arranging structural engineer for the site</li>
  </ul>
  <ul class="tasks" style="left:143px">
    <li><svg viewBox="0 0 10 10"><circle cx="5" cy="5" r="5" fill="#1f3b53"/><path d="M2.8 5.2l1.5 1.5 3-3.2" stroke="#fff" stroke-width="1.1" fill="none"/></svg>Arranging Building control for the site</li>
    <li><svg viewBox="0 0 10 10"><circle cx="5" cy="5" r="5" fill="#1f3b53"/><path d="M2.8 5.2l1.5 1.5 3-3.2" stroke="#fff" stroke-width="1.1" fill="none"/></svg>Making sure material is on site on time</li>
    <li><svg viewBox="0 0 10 10"><circle cx="5" cy="5" r="5" fill="#1f3b53"/><path d="M2.8 5.2l1.5 1.5 3-3.2" stroke="#fff" stroke-width="1.1" fill="none"/></svg>Making sure all tradesman work is up to current British standards</li>
    <li><svg viewBox="0 0 10 10"><circle cx="5" cy="5" r="5" fill="#1f3b53"/><path d="M2.8 5.2l1.5 1.5 3-3.2" stroke="#fff" stroke-width="1.1" fill="none"/></svg>Daily walk rounds to check work is done according to approved plans</li>
    <li><svg viewBox="0 0 10 10"><circle cx="5" cy="5" r="5" fill="#1f3b53"/><path d="M2.8 5.2l1.5 1.5 3-3.2" stroke="#fff" stroke-width="1.1" fill="none"/></svg>Placing orders for bathrooms, kitchen, and flooring</li>
    <li><svg viewBox="0 0 10 10"><circle cx="5" cy="5" r="5" fill="#1f3b53"/><path d="M2.8 5.2l1.5 1.5 3-3.2" stroke="#fff" stroke-width="1.1" fill="none"/></svg>All snag work with main contractor</li>
  </ul>
  <div class="footer" style="left:15px;width:333px"><span>Page 2</span><span>Brelvon Design Solution</span></div>
</section>

<!-- Project 1 -->
<section class="slide col-l r2">
  <div class="tab">PROJECTS 1</div>
  <div class="photo" role="img" aria-label="Row of brick garages with green timber doors" style="left:19px;top:35px;width:197px;height:128px;background:linear-gradient(160deg,#c9ced2 0%,#8f4f3c 35%,#6b5a40 70%,#4f5a3c 100%)"></div>
  <div class="location" style="left:220px;top:48px;width:125px">Garages at Larkfield Mews, Larkfield Street, Kelford</div>
  <p class="proposal" style="left:222px;top:85px;width:120px"><b>Proposal:</b> Change of use from garages to two dwelling houses (use class C3) including alterations to the front and side elevations</p>
  <div class="footer"><span>Page 3</span><span>Brelvon Design Solution</span></div>
</section>

<!-- Project 2 -->
<section class="slide col-r r2">
  <div class="tab">PROJECTS 2</div>
  <div class="location" style="left:132px;top:10px">Location: 58 Ashcombe Road, Kelford</div>
  <p class="proposal" style="left:134px;top:22px;width:200px"><b>Proposal:</b> Change of use from offices (use class B1) to 12 flats (use class C3)</p>
  <div class="photo" role="img" aria-label="Red brick office building behind a large tree" style="left:15px;top:43px;width:160px;height:119px;background:linear-gradient(180deg,#b9c0b4 0%,#5f6e3e 40%,#8a4b3a 65%,#8d8a84 100%)"></div>
  <div class="photo" role="img" aria-label="Side view of the brick building with parked car" style="left:181px;top:43px;width:160px;height:119px;background:linear-gradient(180deg,#9aa69a 0%,#4f6234 40%,#8a4738 65%,#908d88 100%)"></div>
  <div class="footer"><span>Page 4</span><span>Brelvon Design Solution</span></div>
</section>

<!-- Project 2 floor plan -->
<section class="slide col-l r3">
  <div class="tab wide">PROJECTS 2 Floor Plan</div>
  <div class="location" style="left:15px;top:50px;width:95px">Location: 58 Ashcombe Road, Kelford</div>
  <p class="proposal" style="left:17px;top:85px;width:105px"><b>Proposal:</b> Change of use from offices (use class B1) to 12 flats (use class C3)</p>
  <div class="drawing" role="img" aria-label="Ground, first and second floor plans with roof plan and title block" style="left:134px;top:16px;width:208px;height:143px"></div>
  <div class="footer"><span>Page 5</span><span>Brelvon Design Solution</span></div>
</section>

<!-- Project 3 -->
<section class="slide col-r r3">
  <div class="tab">PROJECTS 3</div>
  <div class="location" style="left:15px;top:43px;width:110px">Location: 41-45 Mill Street Kelford</div>
  <p class="proposal" style="left:15px;top:70px;width:100px">
    <b>Proposal:</b> Refurbishment Of Commercial Ground Floor Units Together With Formation Of 6 Residential Units On First And Second Floors. Installation Of Glazing And Repair To External Masonry Including Bricking Up Of Existing Openings</p>
  <div class="photo" role="img" aria-label="Rendered gable wall above shop fronts" style="left:133px;top:17px;width:103px;height:150px;background:linear-gradient(180deg,#c7cbcd 0%,#8c8676 25%,#7f7866 65%,#7b4e3a 85%,#3e4248 100%)"></div>
  <div class="photo" role="img" aria-label="Street view of the corner building" style="left:241px;top:17px;width:103px;height:73px;background:linear-gradient(180deg,#c9ced3 0%,#8a8472 45%,#6a5446 75%,#5a5d60 100%)"></div>
  <div class="photo" role="img" aria-label="Street view along the terrace" style="left:241px;top:95px;width:103px;height:73px;background:linear-gradient(180deg,#d2d6da 0%,#8e8877 45%,#7a4d3c 75%,#55585c 100%)"></div>
  <div class="footer"><span>Page 6</span><span>Brelvon Design Solution</span></div>
</section>

<!-- Project 3 floor plan -->
<section class="slide col-l r4">
  <div class="tab wide">PROJECTS 3 Floor Plan</div>
  <div class="drawing" role="img" aria-label="Coloured floor plans showing retail units and six flats with fire safety legend" style="left:15px;top:38px;width:327px;height:127px;background:#f6f3d6"></div>
  <div class="footer"><span>Page 7</span><span>Brelvon Design Solution</span></div>
</section>

<!-- Project 4 -->
<section class="slide col-r r4">
  <div class="tab">PROJECTS 4</div>
  <div class="location" style="left:15px;top:43px;width:105px">Location: Land at 3 Oakfield Kelford KE4 2RT</div>
  <p class="proposal" style="left:15px;top:77px;width:110px"><b>Proposal:</b> Erection of a dwelling house (use class C3)</p>
  <div class="photo" role="img" aria-label="Completed brick and render detached house" style="left:132px;top:10px;width:212px;height:80px;background:linear-gradient(180deg,#5f7d4a 0%,#d9d4cc 35%,#8b4a38 65%,#5a5a5a 100%)"></div>
  <div class="drawing" role="img" aria-label="House floor plans and site plan" style="left:15px;top:100px;width:91px;height:70px"></div>
  <div class="fp-title" style="left:111px;top:120px">PROJECT<br>FLOOR<br>PLAN</div>
  <div class="elev-label" style="left:272px;top:99px">PROPOSED ELEVATION HOUSE</div>
  <div class="drawing" role="img" aria-label="Proposed front elevation of the house with material notes" style="left:185px;top:104px;width:160px;height:66px;background:linear-gradient(180deg,#6b6b6b 0%,#e9e6e2 45%,#8a4a3a 100%)"></div>
  <div class="footer"><span>Page 8</span><span>Brelvon Design Solution</span></div>
</section>

<!-- Project 5 -->
<section class="slide col-l r5">
  <div class="tab">PROJECTS 5</div>
  <div class="location" style="left:15px;top:34px;width:110px">Location: 12, Tanner Street, Halbrook</div>
  <p class="proposal" style="left:15px;top:59px;width:105px"><b>Proposal:</b> Warehouse conversion to 4 town houses.</p>
  <div class="drawing" role="img" aria-label="Town house floor plans" style="left:15px;top:84px;width:108px;height:82px;background:#fafafa"></div>
  <div class="photo" role="img" aria-label="Victorian brick warehouse facade with shutters" style="left:203px;top:4px;width:145px;height:166px;background:linear-gradient(180deg,#7a4638 0%,#8e4d3c 50%,#5d3f35 80%,#4b4b4b 100%)"></div>
  <div class="photo" role="img" aria-label="Courtyard of the brick warehouse under blue sky" style="left:128px;top:52px;width:107px;height:117px;border:2px solid #fff;background:linear-gradient(170deg,#5d8fd0 0%,#9b5a44 35%,#7b4537 70%,#6d6d6d 100%)"></div>
  <div class="footer"><span>Page 9</span><span>Brelvon Design Solution</span></div>
</section>

<!-- Thank you -->
<section class="slide col-r r5 thanks">
  <div class="mark-name">Brelvon Design Solution</div>
  <div class="word" style="top:50px">THANK</div>
  <div class="word" style="top:106px">YOU</div>
</section>
</body>
</html>
```